Luxury Lifestyle Website - Blog and Product Showcasing

I am looking to create a simple, yet elegant website where I can post blog posts and feature products and brand partnerships for my company, Velmora Haus. I want a very elegant but not overly complex site. I like the look and feel of Corinne Ashdale's site - I don't need for it to be that robust or sophisticated, but that is the aesthetic I am going for. I would like to include my primary logo at the top of the main page, and also incorporate my alternative logos throughout the site in strategic places.

Target Market(s)

Luxury Brands; 20s-60s year olds; women; high-end fashion and tastes

Industry/Entity Type

Luxury Lifestyle - Blogging - Product Showcasing

Coding

Coded - Design and coding required

Number of Pages Required

4 page

Font styles to use
Sans Serif
Script
Other font styles liked:
• Pinyon

Colors
00AB8E
00BBA5
67D7C9
C6EFE9
E9F9F6
59FF00
82FF00
B8FF75
E3FFCB
F4FFEA

Requirements
Must have
• Creative use of my various logos. PASTEL GREENS or a DEEP DARK GREEN. Nothing bright, very soft and elegant.
Nice to have
• Elegant script that is easy to read.
Should not have
• Bright colors or overly modern look or feel.

```html
<!DOCTYPE html>
<html lang="en">
<head>
<meta charset="utf-8">
<title>Velmora Haus — Luxury Lifestyle</title>
<link href="https://fonts.googleapis.com/css2?family=Lato:wght@400;700&family=Pinyon+Script&display=swap" rel="stylesheet">
<style>
  :root {
    --teal: #00AB8E;
    --teal-2: #00BBA5;
    --mint: #67D7C9;
    --mint-pale: #C6EFE9;
    --mint-wash: #EFF9F7;
    --ink: #111111;
    --text: #6a6a6a;
    --white: #ffffff;
    --black: #000000;
  }
  * { box-sizing: border-box; margin: 0; padding: 0; }
  html, body { width: 1200px; height: 4862px; overflow: hidden; }
  body { position: relative; background: var(--white); font-family: 'Lato', sans-serif; color: var(--text); }
  .abs { position: absolute; }
  .script { font-family: 'Pinyon Script', cursive; color: var(--ink); font-weight: 400; }
  .script em { font-style: normal; color: var(--teal); }

  .top-rule { left: 0; top: 0; width: 1200px; height: 4px; background: var(--teal); }
  .menu-toggle { left: 1066px; top: 34px; width: 22px; height: 18px; }
  .menu-toggle span { display: block; height: 2px; background: var(--ink); margin-bottom: 5px; margin-left: auto; }

  .hero-art { left: 58px; top: 38px; width: 620px; height: 600px;
    border-radius: 38% 62% 30% 70% / 35% 40% 60% 65%;
    background: radial-gradient(ellipse at 38% 40%, #c81f3a 0%, #e0485e 25%, #f08e86 48%, #f7c29f 68%, rgba(252,236,222,.6) 85%, rgba(255,255,255,0) 100%);
    opacity: .88; }

  .brand { left: 630px; top: 136px; width: 400px; text-align: center; }
  .brand .mark { display: inline-block; width: 70px; height: 70px; border: 2px solid #555; margin-bottom: 20px; }
  .brand .name { font-size: 30px; letter-spacing: 3px; color: #555; font-weight: 400; }
  .brand .tag { font-size: 9px; letter-spacing: 6px; color: #555; margin-top: 6px; }

  .hero-title { left: 517px; top: 318px; width: 600px; text-align: center; font-size: 66px; line-height: 70px; white-space: nowrap; }
  .btn { display: inline-flex; align-items: center; justify-content: center; background: var(--teal); color: var(--white); font-weight: 700; font-size: 16px; text-decoration: none; }
  .hero-btn { left: 762px; top: 575px; width: 131px; height: 42px; font-style: italic; }
  .hero-wave { left: 0; top: 620px; width: 1200px; height: 140px; }

  .section-title { left: 0; width: 1200px; text-align: center; font-size: 46px; }
  .section-intro { left: 150px; width: 900px; text-align: center; font-size: 15px; line-height: 30px; }

  .service { width: 312px; text-align: center; }
  .service h3 { font-size: 17px; font-weight: 700; color: var(--ink); height: 46px; }
  .service .photo { width: 312px; height: 378px; }
  .read-more { display: inline-block; font-size: 14px; font-weight: 700; color: var(--teal); text-decoration: underline; margin-top: 28px; }

  .about { left: 0; top: 1606px; width: 1200px; height: 600px; }
  .about .panel { position: absolute; left: 0; top: 0; width: 600px; height: 600px; background: var(--mint-wash); }
  .about .photo { position: absolute; left: 600px; top: 0; width: 600px; height: 600px;
    background: linear-gradient(135deg, #c96f8e 0%, #e3a4b7 35%, #9a5a4e 60%, #3f3a22 100%); }
  .about h2 { position: absolute; left: 111px; top: 88px; font-size: 46px; }
  .about p { position: absolute; left: 111px; width: 420px; font-size: 14.5px; line-height: 30px; white-space: nowrap; }
  .about .btn { position: absolute; left: 111px; top: 470px; width: 129px; height: 41px; }

  .post { width: 311px; }
  .post .photo { position: relative; width: 311px; height: 212px; }
  .post .date { position: absolute; left: 28px; top: 189px; width: 127px; height: 42px; background: var(--teal-2); color: var(--white); font-weight: 700; font-size: 16px; display: flex; align-items: center; justify-content: center; }
  .post h3 { margin: 46px 0 0 12px; font-size: 16.5px; line-height: 30px; font-weight: 700; color: var(--ink); white-space: nowrap; }
  .post p { margin: 8px 0 0 12px; font-size: 12px; line-height: 21px; white-space: nowrap; }
  .post .read-more { margin: 18px 0 0 12px; }

  .video { left: 111px; top: 3051px; width: 978px; height: 430px; border-radius: 8px; box-shadow: 0 4px 18px rgba(0,0,0,.18);
    background: linear-gradient(180deg, #f6e7c4 0%, #e8c48a 30%, #a98a7a 55%, #5d5a36 80%, #3b3a22 100%); }
  .play { left: 572px; top: 3238px; width: 56px; height: 56px; }

  .gram { width: 223px; height: 319px; border-radius: 50%; }

  .footer-wave { left: 0; top: 4190px; width: 1200px; height: 672px; }
  .footer-brand { left: 0; top: 4463px; width: 1200px; text-align: center; }
  .footer-brand .mark { display: inline-block; width: 70px; height: 70px; border: 2px solid var(--teal); margin-bottom: 22px; }
  .footer-brand .name { font-size: 34px; color: var(--teal); letter-spacing: 2px; }
  .footer-brand .tag { font-size: 9px; color: var(--teal); letter-spacing: 6px; margin-top: 6px; }
  .footer-nav { left: 0; top: 4699px; width: 1200px; height: 24px; }
  .footer-nav a, .footer-nav span { position: absolute; top: 0; transform: translateX(-50%); color: var(--white); font-weight: 700; font-size: 16.5px; text-decoration: none; white-space: nowrap; }
  .social { top: 4759px; width: 30px; height: 30px; border-radius: 50%; background: var(--teal); }
  .copyright { left: 0; top: 4818px; width: 1200px; text-align: center; color: var(--white); font-size: 11px; }
</style>
</head>
<body>

<header>
  <div class="abs top-rule"></div>
  <div class="abs menu-toggle" aria-label="Menu"><span style="width:22px"></span><span style="width:16px"></span><span style="width:22px"></span></div>
  <div class="abs hero-art" role="img" aria-label="Watercolour illustration of a dancing woman in red and orange washes"></div>
  <div class="abs brand">
    <div class="mark"></div>
    <div class="name">VELMORA HAUS</div>
    <div class="tag">LUXURY LIFESTYLE</div>
  </div>
  <h1 class="abs script hero-title">The Authority on<br>Living an <em>Elegantly</em><br><em>Extravagant</em> Existence</h1>
  <a class="abs btn hero-btn" href="#">Get Started</a>
  <svg class="abs hero-wave" viewBox="0 0 1200 140" preserveAspectRatio="none">
    <path d="M0,22 C320,80 700,150 1200,40 L1200,72 C780,150 380,130 0,46 Z" fill="var(--teal)"/>
  </svg>
</header>

<section class="services">
  <h2 class="abs script section-title" style="top:846px">Our <em>Services</em></h2>
  <p class="abs section-intro" style="top:916px">Sed ut perspiciatis unde omnis iste natus error sit voluptatem accusantium doloremque laudantium, totam rem<br>aperiam, eaque ipsa quae ab illo inventore veritatis et quasi architecto beatae vitae dicta sunt explicabo.</p>
  <div class="abs service" style="left:94px;top:1033px">
    <h3>LOREM LIPSUM DUMMY</h3>
    <div class="photo" role="img" aria-label="Woman in a straw hat and floral dress by a wooden wall" style="background:linear-gradient(160deg,#8a7f6e,#d9c9b0 50%,#6d5a4a)"></div>
    <a class="read-more" href="#">Read More</a>
  </div>
  <div class="abs service" style="left:443px;top:1033px">
    <h3>LOREM LIPSUM DUMMY</h3>
    <div class="photo" role="img" aria-label="Woman in a dark cowboy hat and red dress" style="background:linear-gradient(160deg,#d7c2c4,#c7524a 55%,#8f2d2a)"></div>
    <a class="read-more" href="#">Read More</a>
  </div>
  <div class="abs service" style="left:792px;top:1033px">
    <h3>LOREM LIPSUM DUMMY</h3>
    <div class="photo" role="img" aria-label="Woman in a brown vest seated on hay bales" style="background:linear-gradient(160deg,#bfa07a,#6b4d36 55%,#2f3545)"></div>
    <a class="read-more" href="#">Read More</a>
  </div>
</section>

<section class="abs about">
  <div class="panel"></div>
  <div class="photo" role="img" aria-label="Red-haired woman in a pink dress among blossoming trees"></div>
  <h2 class="script">About <em>Us</em></h2>
  <p style="top:166px">Sed ut perspiciatis unde omnis iste natus error sit voluptatem<br>accusantium doloremque laudantium, totam rem aperiam,<br>eaque ipsa quae ab illo inventore veritatis et quasi architecto<br>beatae vitae dic</p>
  <p style="top:316px">ta sunt explicabo. Nemo enim ipsam voluptatem quia voluptas<br>sit aspernatur aut odit aut fugit, sed quia consequuntur magni<br>dolores eos qui ratione voluptatem sequi nesciunt. Neque<br>porro quisquam est, qui dolorem</p>
  <a class="btn" href="#">Read More</a>
</section>

<section class="posts">
  <h2 class="abs script section-title" style="top:2303px">Latest <em>Posts</em></h2>
  <p class="abs section-intro" style="top:2373px">Sed ut perspiciatis unde omnis iste natus error sit voluptatem accusantium doloremque laudantium, totam rem<br>aperiam, eaque ipsa quae ab illo inventore veritatis et quasi architecto beatae vitae dicta sunt explicabo.</p>
  <article class="abs post" style="left:98px;top:2483px">
    <div class="photo" role="img" aria-label="Woman in a sun hat by a lake in golden light" style="background:linear-gradient(180deg,#c9b9a2,#e9d9b8 50%,#cdb07a)"><div class="date">July 17</div></div>
    <h3>Sed ut perspiciatis unde omnis iste nat<br>us error sit voluptatem</h3>
    <p>I must explain to you how all this mistaken idea of<br>denouncing pleasure and praising pain was born<br>and I will give you a complete account of the<br>system, and expound the</p>
    <a class="read-more" href="#">Read More</a>
  </article>
  <article class="abs post" style="left:445px;top:2483px">
    <div class="photo" role="img" aria-label="Laughing woman in front of a wall of pink roses" style="background:linear-gradient(180deg,#e6b9bd,#f0dcd9 50%,#d9c6c3)"><div class="date">July 17</div></div>
    <h3>Sed ut perspiciatis unde omnis iste nat<br>us error sit voluptatem</h3>
    <p>I must explain to you how all this mistaken idea of<br>denouncing pleasure and praising pain was born<br>and I will give you a complete account of the<br>system, and expound the</p>
    <a class="read-more" href="#">Read More</a>
  </article>
  <article class="abs post" style="left:791px;top:2483px">
    <div class="photo" role="img" aria-label="Woman in a patterned dress in a green tropical garden" style="background:linear-gradient(180deg,#2f4a2e,#486b3d 50%,#243624)"><div class="date">July 17</div></div>
    <h3>Sed ut perspiciatis unde omnis iste nat<br>us error sit voluptatem</h3>
    <p>I must explain to you how all this mistaken idea of<br>denouncing pleasure and praising pain was born<br>and I will give you a complete account of the<br>system, and expound the</p>
    <a class="read-more" href="#">Read More</a>
  </article>
</section>

<section class="media">
  <div class="abs video" role="img" aria-label="Video still of a woman in a cream dress walking through a field of lupins at sunset"></div>
  <svg class="abs play" viewBox="0 0 56 56" aria-label="Play video">
    <circle cx="28" cy="28" r="27" fill="#e23b3b" stroke="#fff" stroke-width="2"/>
    <path d="M22,17 L39,28 L22,39 Z" fill="#fff"/>
  </svg>
</section>

<section class="social-feed">
  <h2 class="abs script section-title" style="top:3583px">Follow Us On <em>Social</em></h2>
  <p class="abs section-intro" style="top:3654px">Sed ut perspiciatis unde omnis iste natus error sit voluptatem accusantium doloremque laudantium, totam rem<br>aperiam, eaque ipsa quae ab illo inventore veritatis et quasi architecto beatae vitae dicta sunt explicabo.</p>
  <div class="abs gram" style="left:0;top:3761px;background:linear-gradient(180deg,#f1c9bf,#b88a86 55%,#6d4d4c)" role="img" aria-label="Woman with flowing hair in a hazy pink sunset"></div>
  <div class="abs gram" style="left:243px;top:3821px;background:linear-gradient(180deg,#d9a7b8,#e7c7d2 50%,#7d5f67)" role="img" aria-label="Woman twirling a pink gown in a blossom field"></div>
  <div class="abs gram" style="left:487px;top:3761px;background:linear-gradient(180deg,#f3efe8,#e7dccd 50%,#c2b39a)" role="img" aria-label="Laughing woman in a white hat and lace dress"></div>
  <div class="abs gram" style="left:732px;top:3821px;background:linear-gradient(180deg,#c9c0a6,#e4d6c0 50%,#a49179)" role="img" aria-label="Woman in a cream wrap dress in a garden"></div>
  <div class="abs gram" style="left:976px;top:3761px;background:linear-gradient(180deg,#dfe8ee,#f1d6dc 50%,#d59aa7)" role="img" aria-label="Woman in a floral sundress and hat by the sea"></div>
</section>

<footer>
  <svg class="abs footer-wave" viewBox="0 0 1200 672" preserveAspectRatio="none">
    <path d="M0,112 C320,-10 720,10 1200,170 L1200,672 L0,672 Z" fill="var(--teal)"/>
    <path d="M0,150 C360,70 760,90 1200,190 L1200,672 L0,672 Z" fill="var(--black)"/>
  </svg>
  <div class="abs footer-brand">
    <div class="mark"></div>
    <div class="name">VELMORA HAUS</div>
    <div class="tag">LUXURY LIFESTYLE</div>
  </div>
  <nav class="abs footer-nav">
    <a href="#" style="left:213px">Home</a><span style="left:287px">|</span>
    <a href="#" style="left:377px">About Us</a><span style="left:464px">|</span>
    <a href="#" style="left:568px">Our Services</a><span style="left:670px">|</span>
    <a href="#" style="left:772px">Latest Blogs</a><span style="left:870px">|</span>
    <a href="#" style="left:966px">Contact Us</a>
  </nav>
  <div class="abs social" style="left:547px" aria-label="Social link"></div>
  <div class="abs social" style="left:585px" aria-label="Social link"></div>
  <div class="abs social" style="left:625px" aria-label="Social link"></div>
  <p class="abs copyright">© Copyright 2023 &nbsp;| All Rights Reserved</p>
</footer>

</body>
</html>
```